Etiketten für Obsthof in Friedrichshafen am Bodensee
Zielgruppe
Wir sind ein Obsthof in Friedrichshafen am Bodensee und verkaufen in unserem Hofladen unsere selbsthergestellten Produkte. Dabei zeichnet uns besonders aus, dass wir unsere Produkte aus eigens angebautem Obst Herstellen wie zum Beispiel Marmeladen, Säfte, Sirup, Schnaps oder Liköre.
Unsere Zielgruppe sind Kundinnen und Kunden, die Wert auf Regionalität, Transparenz bei der Produktherstellung und Qualität der Inhaltsstoffe legen.
Aufgabenstellung
Uns ist besonders wichtig, dass die Etiketten widerspiegeln, dass die Produkte selbst hergestellt wurden und hochwertig sind.
Die Etiketten sollten alle auf einander abgestimmt sein, sodass sie sich wie eine klare Linie durch das ganze Sortiment ziehen. Dementsprechend soll ein universelles Etikett erstellt werden, das wir für alle unsere Produkte verwenden können. Hierbei ist es wichtig, dass wir im Nachhinein selbst die Produktbeschreibung auf dem Etikett an das jeweilige Produkt anpassen können.
Es sollte auch Platz sein für die Inhaltsstoffe, unsere Anschrift, Mindesthaltbarkeitsdatum und die Inhaltsmenge.
https://www.wendrahof-polmit.com/hofladen-und-produkte.htm
in diese Richtung könnte ich mir die Ausführung vorstellen.

```html
<!DOCTYPE html>
<html lang="de">
<head>
<meta charset="utf-8">
<title>Wendra Obsthof – Etiketten</title>
<link rel="stylesheet" href="https://fonts.googleapis.com/css2?family=Patrick+Hand&family=Caveat&display=swap">
<style>
  :root {
    --bg: #f2f2f2;
    --cream: #f6eed8;
    --green-dark: #2f6b50;
    --leaf-light: #a6d14f;
    --leaf-mid: #7fb636;
    --ink: #1c1c1c;
  }
  html, body {
    margin: 0;
    padding: 0;
    width: 1200px;
    height: 849px;
    overflow: hidden;
    background: var(--bg);
  }
  .label-row {
    position: absolute;
    top: 225px;
    left: 60px;
    width: 1080px;
    display: flex;
    justify-content: space-between;
  }
  .label {
    position: relative;
    width: 320px;
    height: 390px;
    background: var(--cream);
    border-radius: 20px;
    overflow: hidden;
  }
  .label__foliage {
    position: absolute;
    top: 0;
    left: 0;
    right: 0;
    height: 74px;
    background: linear-gradient(180deg, var(--leaf-mid) 0%, var(--leaf-light) 70%, rgba(166,209,79,0.0) 100%);
    border-radius: 20px 20px 0 0;
  }
  .label__frame {
    position: absolute;
    top: 58px;
    left: 22px;
    right: 22px;
    bottom: 22px;
    border: 2px dashed var(--green-dark);
    border-radius: 8px;
  }
  .brand {
    position: absolute;
    top: 88px;
    left: 0;
    right: 0;
    display: flex;
    align-items: center;
    justify-content: center;
    gap: 12px;
  }
  .brand__dot {
    width: 44px;
    height: 44px;
    border-radius: 50%;
    border: 2px solid var(--green-dark);
    box-sizing: border-box;
  }
  .brand__name {
    font-family: "Patrick Hand", cursive;
    font-size: 34px;
    line-height: 0.9;
    color: var(--green-dark);
  }
  .claim {
    position: absolute;
    top: 160px;
    left: 50%;
    transform: translateX(-50%);
    width: 190px;
    height: 40px;
  }
  .claim text {
    font-family: "Patrick Hand", cursive;
    font-size: 13px;
    fill: var(--green-dark);
    letter-spacing: 0.5px;
  }
  .product {
    position: absolute;
    top: 198px;
    left: 0;
    right: 0;
    text-align: center;
    font-family: "Patrick Hand", cursive;
    font-size: 56px;
    line-height: 0.98;
    color: var(--ink);
  }
  .product--long { font-size: 50px; }
  .volume {
    position: absolute;
    bottom: 10px;
    left: 50%;
    transform: translateX(-50%);
    padding: 0 8px;
    background: var(--cream);
    font-family: "Caveat", cursive;
    font-size: 24px;
    line-height: 24px;
    color: var(--ink);
    white-space: nowrap;
  }
</style>
</head>
<body>
<main class="label-row">

  <article class="label">
    <div class="label__foliage" role="img" aria-label="Gezeichnetes grünes Blätterband am oberen Rand"></div>
    <div class="label__frame"></div>
    <div class="brand">
      <span class="brand__dot"></span>
      <span class="brand__name">Wendra<br>Obsthof</span>
    </div>
    <svg class="claim" viewBox="0 0 190 40" aria-hidden="false">
      <path id="arc1" d="M10 36 Q95 0 180 36" fill="none"/>
      <text><textPath href="#arc1" startOffset="50%" text-anchor="middle">100% aus eigenem Anbau</textPath></text>
    </svg>
    <h2 class="product">Holunder<br>Sirup</h2>
    <span class="volume">500 ml e</span>
  </article>

  <article class="label">
    <div class="label__foliage" role="img" aria-label="Gezeichnetes grünes Blätterband am oberen Rand"></div>
    <div class="label__frame"></div>
    <div class="brand">
      <span class="brand__dot"></span>
      <span class="brand__name">Wendra<br>Obsthof</span>
    </div>
    <svg class="claim" viewBox="0 0 190 40">
      <path id="arc2" d="M10 36 Q95 0 180 36" fill="none"/>
      <text><textPath href="#arc2" startOffset="50%" text-anchor="middle">100% aus eigenem Anbau</textPath></text>
    </svg>
    <h2 class="product">Walnuss<br>Likör</h2>
    <span class="volume">500 ml e</span>
  </article>

  <article class="label">
    <div class="label__foliage" role="img" aria-label="Gezeichnetes grünes Blätterband am oberen Rand"></div>
    <div class="label__frame"></div>
    <div class="brand">
      <span class="brand__dot"></span>
      <span class="brand__name">Wendra<br>Obsthof</span>
    </div>
    <svg class="claim" viewBox="0 0 190 40">
      <path id="arc3" d="M10 36 Q95 0 180 36" fill="none"/>
      <text><textPath href="#arc3" startOffset="50%" text-anchor="middle">100% aus eigenem Anbau</textPath></text>
    </svg>
    <h2 class="product product--long">Sauerkirsch<br>Konfitüre</h2>
    <span class="volume">350 ml</span>
  </article>

</main>
</body>
</html>
```